Erstellung eines Polizeiwimpels für Kinder
Zielgruppe
Wir stellen Fahrradwimpel für Kinder her. Hier finden Sie unsere Produkte: https://www.kramladen.de/stores/node/58203916472
Aufgabenstellung
Wir möchten einen 'Polizeiwimpel' für Kinder herstellen.
Wenn möglich, nur eine Farbe verwenden (reduziert Kosten in der Produktion). Der Hintergrund soll 'Polizei Blau' sein.
Wimpelgröße: 17,5 cm X 32 cm X 32cm (Dreieckig)
Ich habe ein selbst erstelltes Design hochgeladen. Es soll den Schriftzug 'Polizei' enthalten und evtl. noch 'Polizei Symbole', die Jungs (und ihre Eltern) ansprechen. (Pistole, Sheriffstern, etc.) Das offizielle Wappen oder andere Hoheitssymbole dürfen wir allerdings nicht verwenden.

```html
<!DOCTYPE html>
<html lang="de">
<head>
<meta charset="utf-8">
<title>Polizeiwimpel für Kinder</title>
<link rel="stylesheet" href="https://fonts.googleapis.com/css2?family=Arimo:wght@400;700&display=swap">
<style>
  :root {
    --police-blue: #1d6fb8;
    --pennant-grey: #dcdcdc;
    --page-white: #ffffff;
  }
  html, body {
    margin: 0;
    padding: 0;
    width: 1200px;
    height: 656px;
    overflow: hidden;
    background: var(--page-white);
  }
  .pennant {
    display: block;
    width: 1200px;
    height: 656px;
  }
  .pennant__base { fill: var(--pennant-grey); }
  .pennant__band { fill: var(--police-blue); }
  .pennant__dash { fill: var(--pennant-grey); }
  .pennant__title {
    font-family: "Arimo", Arial, sans-serif;
    font-weight: 700;
    font-size: 160px;
    fill: var(--pennant-grey);
  }
  .pennant__cap { fill: var(--pennant-grey); }
  .pennant__web {
    font-family: "Arimo", Arial, sans-serif;
    font-weight: 400;
    font-size: 14px;
    fill: var(--police-blue);
  }
</style>
</head>
<body>
  <svg class="pennant" viewBox="0 0 1200 656" xmlns="http://www.w3.org/2000/svg" aria-label="Fahrradwimpel Polizei">
    <defs>
      <clipPath id="pennant-shape">
        <polygon points="0,0 1200,324 0,656"/>
      </clipPath>
    </defs>

    <polygon class="pennant__base" points="0,0 1200,324 0,656"/>

    <g clip-path="url(#pennant-shape)">
      <rect class="pennant__band" x="0" y="119" width="1200" height="416"/>

      <g class="pennant__road-line pennant__road-line--top">
        <rect class="pennant__dash" x="7"   y="193" width="73" height="25"/>
        <rect class="pennant__dash" x="104" y="193" width="75" height="25"/>
        <rect class="pennant__dash" x="202" y="193" width="78" height="25"/>
        <rect class="pennant__dash" x="301" y="193" width="78" height="25"/>
        <rect class="pennant__dash" x="400" y="193" width="80" height="25"/>
        <rect class="pennant__dash" x="502" y="193" width="77" height="25"/>
        <rect class="pennant__dash" x="601" y="193" width="77" height="25"/>
        <rect class="pennant__dash" x="700" y="193" width="77" height="25"/>
      </g>

      <g class="pennant__road-line pennant__road-line--bottom">
        <rect class="pennant__dash" x="7"   y="449" width="73" height="28"/>
        <rect class="pennant__dash" x="104" y="449" width="75" height="28"/>
        <rect class="pennant__dash" x="202" y="449" width="78" height="28"/>
        <rect class="pennant__dash" x="301" y="449" width="78" height="28"/>
        <rect class="pennant__dash" x="400" y="449" width="80" height="28"/>
        <rect class="pennant__dash" x="502" y="449" width="77" height="28"/>
        <rect class="pennant__dash" x="601" y="449" width="77" height="28"/>
        <rect class="pennant__dash" x="700" y="449" width="77" height="28"/>
      </g>
    </g>

    <text class="pennant__title" x="38" y="394" textLength="643" lengthAdjust="spacingAndGlyphs">POLIZEI</text>

    <rect class="pennant__cap" x="735" y="290" width="200" height="108" rx="36"
          role="img" aria-label="Polizeimütze mit Stern"/>

    <text class="pennant__web" x="40" y="621">www.wimpel-muster.example</text>
  </svg>
</body>
</html>
```